VarnLink Signal Systems Website Design

We are an Australian based telecommunications company who specialise in the design, build and implementation of mission critical communications infrastructure. We have offices throughout Australia, New Zealand and Europe. Our Customers are operators in multiple markets from Oil & Gas, Mining, Government, Utilities, Carrier & Transportation.

We also work with large multi-national companies, that provide telecommunication and services such as; Pelvaro, Dransvik, Quorba, Talmoss and many more. We want to be able to achieve the same level of impressions and professionalism as what these companies present on their websites.

To reflect our recent move into the European market, we need our new site to reflect who we are as a company, and exhibit the fact we are not just based in Australia, but we are a global organisation. We want to have a fresh clean look, thats modern, dynamic and simple. Flat textures and colours are perfect for us to adapt to. A site that is based around content management, with a responsive design that can be used on all devices.

We have started to develop a basic design language that we would like to incorporate in our overall website design. We have attached some documents that highlight our design language and we can provide colour codes and fonts to ensure consistency.

Our existing site is: www.varnlinkss.example. Please feel free to view and pick apart items. From this example, we would massive improvement in how the site looks, feels and functions. We also want social media to form a big part of our site, with the likes of posts from chirpnet and blogs posting capabilities.

If you require anymore information about VarnLink or our requirements, please do not hesitate to contact.

Thanks and good luck!

Target Market(s)

Potential & Existing Customers, New international customers & markets, New Market Sectors, Partners, Service Providers

Industry/Entity Type

Telecommunications

Coding

Coded - Design and coding required

Number of Pages Required

5+ page

Font styles to use
Sans Serif

Requirements
Must have
• Content Management, Responsive Design for multiple device compatibility, Social media integration, use of lots of imagery, drop down menus, search capabilities
Should not have
• No flash.

```html
<!DOCTYPE html>
<html lang="en">
<head>
<meta charset="utf-8">
<title>VarnLink Signal Systems</title>
<link rel="stylesheet" href="https://fonts.googleapis.com/css2?family=Nunito+Sans:wght@300;400;600;700;800&display=swap">
<style>
:root{
  --navy:#1f2a4a;
  --ink:#3a3a3a;
  --muted:#6d6d6d;
  --violet:#7774ad;
  --violet-btn:#7a76a8;
  --paper:#f8f8f8;
  --white:#ffffff;
  --cyan:#5fdfee;
  --footer:#46466b;
  --line:#e3e3e3;
}
*{box-sizing:border-box;margin:0;padding:0}
html,body{width:1200px;height:2786px;overflow:hidden}
body{font-family:"Nunito Sans",Arial,sans-serif;color:var(--ink);background:var(--white);position:relative}
.abs{position:absolute}

/* header */
.site-header{position:absolute;left:0;top:0;width:1200px;height:106px;background:var(--white)}
.brand{position:absolute;left:173px;top:38px;display:flex;align-items:center;gap:8px;font-weight:800;font-size:24px;color:var(--navy)}
.brand-dot{width:12px;height:12px;border-radius:50%;background:var(--violet)}
.main-nav{position:absolute;top:46px;left:0;width:1200px;font-size:14px;font-weight:700;color:var(--navy)}
.main-nav span{position:absolute;white-space:nowrap}

/* hero */
.hero{position:absolute;left:0;top:106px;width:1200px;height:479px;background:linear-gradient(160deg,#c9ccd0 0%,#8a9096 35%,#4f5860 60%,#6d7780 100%)}
.hero-title{position:absolute;left:0;width:1200px;top:222px;text-align:center;color:var(--white);font-size:35px;font-weight:700}
.hero-dots{position:absolute;top:433px;left:0;width:1200px;display:flex;justify-content:center;gap:10px}
.hero-dots i{width:8px;height:8px;border-radius:50%;background:var(--white)}

/* market */
.market{position:absolute;left:0;top:585px;width:1200px;height:793px;background:var(--violet)}
.section-title{position:absolute;left:0;width:1200px;text-align:center;font-size:27px;font-weight:800}
.market .section-title{top:40px;color:var(--white)}
.market-intro{position:absolute;left:160px;width:880px;top:98px;text-align:center;color:var(--white);font-size:13px;line-height:22px}
.sector{position:absolute;color:var(--white);font-size:20px;font-weight:300}
.sector span{position:absolute;left:22px;bottom:22px;line-height:24px}
.sector.oil{left:173px;top:221px;width:416px;height:283px;background:linear-gradient(180deg,#6f8fc0,#3c4f6c 70%,#2c3440)}
.sector.mining{left:613px;top:221px;width:414px;height:283px;background:linear-gradient(180deg,#d9d2bd,#b79e5e 60%,#8f7a40)}
.sector.gov{left:173px;top:528px;width:269px;height:197px;background:linear-gradient(180deg,#93a5b8,#4f5c6b 70%,#2c3440)}
.sector.util{left:463px;top:528px;width:269px;height:197px;background:linear-gradient(180deg,#8fb5c9,#5a6a86 60%,#c88f55)}
.sector.carrier{left:758px;top:528px;width:269px;height:197px;background:linear-gradient(180deg,#c6cdd8,#8a8e9e 55%,#b56b4a)}

/* blog */
.blog{position:absolute;left:0;top:1378px;width:1200px;height:603px;background:var(--paper)}
.blog .section-title{top:40px;color:var(--ink)}
.blog-rule{position:absolute;left:173px;top:99px;width:854px;height:1px;background:var(--line)}
.post{position:absolute;top:149px;width:270px;height:407px;background:var(--white);border:1px solid var(--line)}
.post-media{position:absolute;left:13px;top:15px;width:244px;height:180px}
.post-meta{position:absolute;left:13px;top:212px;font-size:10px;color:var(--ink)}
.post-meta b{color:var(--violet)}
.post-heading{position:absolute;left:13px;top:245px;width:244px;font-size:10px;font-weight:700;line-height:15px;color:var(--ink)}
.post-excerpt{position:absolute;left:13px;top:289px;width:244px;font-size:9px;line-height:13px;color:var(--muted)}
.btn-more{position:absolute;left:13px;top:356px;width:67px;height:26px;background:var(--violet-btn);color:var(--white);font-size:9px;font-weight:700;display:flex;align-items:center;justify-content:center}

/* partners */
.partners{position:absolute;left:0;top:1981px;width:1200px;height:171px;background:var(--white)}
.partner{position:absolute;top:64px;transform:translateX(-50%);font-size:22px;font-weight:700;color:var(--navy);white-space:nowrap}

/* social feed */
.feed{position:absolute;left:0;top:2152px;width:1200px;height:317px;background:var(--cyan);color:var(--white)}
.feed-label{position:absolute;left:171px;width:200px;top:140px;text-align:center;font-size:35px;font-weight:300}
.feed-icon{position:absolute;left:257px;top:104px}
.feed-divider{position:absolute;left:409px;top:65px;width:1px;height:213px;background:rgba(255,255,255,.6)}
.avatar{position:absolute;left:444px;top:105px;width:120px;height:120px;border-radius:50%;background:linear-gradient(180deg,#c9b8a3,#8e6a52 60%,#a04a3c)}
.feed-date{position:absolute;left:589px;top:110px;font-size:13px;font-weight:700}
.feed-text{position:absolute;left:589px;top:140px;width:530px;font-size:12px;line-height:19px}
.feed-arrows{position:absolute;left:1025px;top:234px}

/* footer */
.site-footer{position:absolute;left:0;top:2469px;width:1200px;height:317px;background:var(--footer);color:var(--white)}
.footer-brand{position:absolute;left:173px;top:76px;display:flex;align-items:center;gap:8px;font-size:22px;font-weight:800}
.footer-brand .brand-dot{background:var(--white)}
.footer-col{position:absolute;top:58px}
.footer-col h4{font-size:12px;font-weight:800;letter-spacing:.3px;margin-bottom:18px}
.footer-col li{list-style:none;font-size:13px;line-height:22.3px}
.social-links{display:flex;gap:8px;font-size:10px;font-weight:600}
.copyright{position:absolute;left:0;width:1200px;top:283px;text-align:center;font-size:10px;font-weight:600}
</style>
</head>
<body>

<header class="site-header">
  <div class="brand"><span class="brand-dot"></span>VarnLink</div>
  <nav class="main-nav">
    <span style="left:487px">Home</span>
    <span style="left:556px">Products &amp; Services</span>
    <span style="left:715px">Sectors</span>
    <span style="left:793px">Support</span>
    <span style="left:877px">Corporate</span>
    <span style="left:977px">Contact</span>
  </nav>
</header>

<section class="hero" role="img" aria-label="Commuter train arriving at a modern railway station platform">
  <h1 class="hero-title">VarnLink Signal Systems</h1>
  <div class="hero-dots"><i></i><i></i><i></i></div>
</section>

<section class="market">
  <h2 class="section-title">OUR MARKET</h2>
  <p class="market-intro">In 1998, the Directors identified the need for a specialist value added reseller that could provide quality communications systems and services that were more appropriate and better suited to mission critical and industrial applications.As a result, VarnLink was formed and with it, a set of important principles that have been the cornerstone of VarnLink's success.</p>
  <div class="sector oil" role="img" aria-label="Oil and gas refinery pipework"><span>Oil &amp; Gas</span></div>
  <div class="sector mining" role="img" aria-label="Loader working in an open-cut mine"><span>Mining</span></div>
  <div class="sector gov" role="img" aria-label="City office towers"><span>Government</span></div>
  <div class="sector util" role="img" aria-label="Power transmission towers at dusk with light trails"><span>Utilities</span></div>
  <div class="sector carrier" role="img" aria-label="Container port cranes and cargo ship"><span>Carrier<br>&amp; Transportation</span></div>
</section>

<section class="blog">
  <h2 class="section-title">BLOG POSTS</h2>
  <div class="blog-rule"></div>

  <article class="post" style="left:173px">
    <div class="post-media" role="img" aria-label="Hand touching a tablet screen" style="background:linear-gradient(135deg,#f2c98a,#c9a6c4 50%,#7b8fb8)"></div>
    <p class="post-meta">Posted By <b>VarnLink Signal Systems</b></p>
    <h3 class="post-heading">Sed ut perspiciatis unde omnis iste natus error sit voluptatem accusantium doloremque ....</h3>
    <p class="post-excerpt">Totam rem aperiam, eaque ipsa quae ab illo inventore veritatis et quasi architecto beatae vitae dicta sunt explicabo. Nemo enim ipsam voluptatem quia voluptas sit aspernatur aut odit aut fugit</p>
    <span class="btn-more">Read More</span>
  </article>

  <article class="post" style="left:465px">
    <div class="post-media" role="img" aria-label="Cloud security concept on a circuit board" style="background:linear-gradient(160deg,#27334f,#3f5d82 55%,#1c2336)"></div>
    <p class="post-meta">Posted By <b>VarnLink Signal Systems</b></p>
    <h3 class="post-heading">Sed ut perspiciatis unde omnis iste natus error sit voluptatem accusantium doloremque ....</h3>
    <p class="post-excerpt">Totam rem aperiam, eaque ipsa quae ab illo inventore veritatis et quasi architecto beatae vitae dicta sunt explicabo. Nemo enim ipsam voluptatem quia voluptas sit aspernatur aut odit aut fugit</p>
    <span class="btn-more">Read More</span>
  </article>

  <article class="post" style="left:756px">
    <div class="post-media" role="img" aria-label="Person using a smartphone" style="background:linear-gradient(135deg,#e9d8cf,#c88f86 55%,#8a6a7a)"></div>
    <p class="post-meta">Posted By <b>VarnLink Signal Systems</b></p>
    <h3 class="post-heading">Sed ut perspiciatis unde omnis iste natus error sit voluptatem accusantium doloremque ....</h3>
    <p class="post-excerpt">Totam rem aperiam, eaque ipsa quae ab illo inventore veritatis et quasi architecto beatae vitae dicta sunt explicabo. Nemo enim ipsam voluptatem quia voluptas sit aspernatur aut odit aut fugit</p>
    <span class="btn-more">Read More</span>
  </article>
</section>

<section class="partners" aria-label="Partners">
  <span class="partner" style="left:215px">Quorba</span>
  <span class="partner" style="left:373px">Morvant</span>
  <span class="partner" style="left:515px">Talmoss</span>
  <span class="partner" style="left:663px">Kelvra</span>
  <span class="partner" style="left:775px">Sindrafall</span>
  <span class="partner" style="left:962px">Pelvaro</span>
</section>

<section class="feed">
  <svg class="feed-icon" width="28" height="28" viewBox="0 0 28 28" aria-hidden="true"><rect x="2" y="2" width="24" height="24" fill="#fff"/></svg>
  <div class="feed-label">chirpnet</div>
  <div class="feed-divider"></div>
  <div class="avatar" role="img" aria-label="Profile photo of the post author"></div>
  <p class="feed-date">Posted On 19-5-2015</p>
  <p class="feed-text">Sed ut perspiciatis unde omnis iste natus error sit voluptatem accusantium doloremque laudantium, totam rem aperiam, eaque ipsa quae ab illo inventore veritatis et quasi architecto beatae vitae dicta sunt explicabo. Nemo enim ipsam voluptatem quia voluptas sit aspernatur aut odit aut fugit, sed quia consequuntur magni dolores</p>
  <svg class="feed-arrows" width="44" height="24" viewBox="0 0 44 24" aria-hidden="true">
    <polyline points="14,5 7,12 14,19" fill="none" stroke="#fff" stroke-width="3"/>
    <polyline points="30,5 37,12 30,19" fill="none" stroke="#fff" stroke-width="3"/>
  </svg>
</section>

<footer class="site-footer">
  <div class="footer-brand"><span class="brand-dot"></span>VarnLink</div>
  <div class="footer-col" style="left:370px">
    <h4>QUICK LINKS</h4>
    <ul><li>Home</li><li>Products &amp; Services</li><li>Sectors</li><li>Support</li><li>Corporate</li><li>Contact</li></ul>
  </div>
  <div class="footer-col" style="left:559px">
    <h4>OTHER LINKS</h4>
    <ul><li>Rapid Site Solution</li><li>OSS</li><li>Responsibilities</li><li>Contact</li></ul>
  </div>
  <div class="footer-col" style="left:739px">
    <h4>SUPPORT LINKS</h4>
    <ul><li>Legal Information</li><li>Privacy policy</li><li>Terms Of Use</li><li>Cookies</li><li>Sitemap</li></ul>
  </div>
  <div class="footer-col" style="left:903px">
    <h4>CONNECT WITH&nbsp; US</h4>
    <div class="social-links"><span>Facelane</span><span>Snapgrid</span><span>Linkwork</span><span>chirpnet</span></div>
  </div>
  <p class="copyright">© 2016 COMPANY NAME | ALL RIGHTS RESERVED</p>
</footer>

</body>
</html>
```